Original catchy book cover

I need a book cover for my book "The Copper Kettle Handbook" (https://quillpress.example/copperkettle). This will be a book self published on marketvale.
The book talks about the following concepts:
- Iterative product delivery
- Early discovery using feedback from customers
- Start small, think big, move fast
- Slice the product into valuable increments that can be validated with customers
- Experimental approach to deciding the next slice of work
A simple cover that stands out from the business books already out there! Some examples are:
https://www.marketvale.example/Tide-Harbor-Steady-Teams-Quietly-ebook/dp/X00AAA1111/ref=sr_1_1?ie=UTF8&qid=1000000001&sr=8-1&keywords=tide+and+harbor
https://www.marketvale.example/Copper-Kettle-Almanac-Brew-Ideas-ebook/dp/X00BBB2222/ref=sr_1_1?s=digital-text&ie=UTF8&qid=1000000002&sr=1-1&keywords=copper+kettle+almanac
https://www.marketvale.example/Orchard-Paths-Rewoven-Compass-Fogbanks-ebook/dp/X00CCC3333/ref=pd_sim_351_2?_encoding=UTF8&psc=1&refRID=ZZZZZZZZZZZZZZZZZZZZ
Lastly, attached are 2 draft covers that i've been playing with. Would love a graphic as part of the cover if it makes sense in your design! The graphic should tie to the meaning or themes of the book. Emphasis on ways of working, collaboration, experimentation, hypothesis, agile, incremental or adaptive. Those are some words that describe the content of the book.
Alternatively, something abstract could also be an option if a literal graphic doesn't suit the theme of your design.
Target Market(s)
Product owners, scrum masters, people in the agile community, software developers, designers
Industry/Entity Type
Information Technology
Font styles to use
Colors
Designer to choose colors to be used in the design.
Requirements
Must have
- Title, Subtitle, Author Name
- Back of the book should have space for a description (use lorem ipsum for now)
- Please use the editorial logo
- (please omit "created by Tomas Verhelst" because the editorial logo replaces that.
- The design must be original art or graphics (i.e. it should be similar to another cover in this topic).
Nice to have
- A graphic would be ideal if it is relevant to the book topic, otherwise a nice simple cover that uses colors or patterns that are easy to recall.
- The color suggestions below are suggestions only. Do not feel you have to incorporate all the colors and feel free to recommend an alternate palette.
Should not have
- Clipart or generic stock art photos. Images for the sake of images, traditional logos (e.g. a computer, a phone etc unless it's part of an overall theme that ties the logos together).

```html
<!DOCTYPE html>
<html lang="en">
<head>
<meta charset="utf-8">
<title>The Copper Kettle Handbook – Cover Wrap</title>
<link rel="stylesheet" href="https://fonts.googleapis.com/css2?family=Bebas+Neue&family=EB+Garamond:wght@400&family=Oswald:wght@200;300&display=swap">
<style>
  :root {
    --magenta: #b0307c;
    --magenta-deep: #a8157f;
    --magenta-spine: #b23a82;
    --ink-magenta: #9e2670;
    --paper: #ffffff;
  }
  * { margin: 0; padding: 0; box-sizing: border-box; }
  html, body {
    width: 1200px;
    height: 830px;
    overflow: hidden;
    background: var(--paper);
  }
  .cover-wrap {
    position: relative;
    width: 1200px;
    height: 830px;
    overflow: hidden;
  }

  /* Back cover */
  .back-cover {
    position: absolute;
    left: 0; top: 0;
    width: 554px; height: 830px;
  }
  .back-artwork {
    position: absolute; inset: 0;
    background:
      radial-gradient(ellipse at 45% 55%, rgba(255,255,255,0.55) 0%, rgba(255,255,255,0) 60%),
      linear-gradient(180deg, #f3d7df 0%, #f7e4ea 45%, #f5dde4 75%, #fbf1f3 100%);
  }
  .back-blurb {
    position: absolute;
    left: 62px; top: 60px;
    width: 434px;
    font-family: "EB Garamond", Georgia, serif;
    font-size: 17.2px;
    line-height: 20px;
    color: var(--ink-magenta);
    text-align: justify;
    hyphens: auto;
  }
  .back-blurb p + p { margin-top: 20px; }
  .isbn-space {
    position: absolute;
    left: 62px; top: 696px;
    width: 132px; height: 86px;
    background: var(--paper);
  }

  /* Spine */
  .spine {
    position: absolute;
    left: 554px; top: 0;
    width: 92px; height: 830px;
    background: var(--magenta-spine);
    color: var(--paper);
  }
  .spine-title {
    position: absolute;
    left: 50%; top: 54px;
    transform: translateX(-50%);
    writing-mode: vertical-rl;
    font-family: "Bebas Neue", Impact, sans-serif;
    font-size: 41px;
    letter-spacing: 2.5px;
    line-height: 1;
    white-space: nowrap;
  }
  .spine-author {
    position: absolute;
    left: 50%; top: 580px;
    transform: translateX(-50%);
    writing-mode: vertical-rl;
    font-family: "Oswald", Arial, sans-serif;
    font-weight: 200;
    font-size: 22px;
    letter-spacing: 7px;
    line-height: 1;
    white-space: nowrap;
  }

  /* Front cover */
  .front-cover {
    position: absolute;
    left: 646px; top: 0;
    width: 554px; height: 830px;
  }
  .front-artwork {
    position: absolute;
    left: 0; top: 408px;
    width: 554px; height: 422px;
    background:
      radial-gradient(ellipse 120px 170px at 48% 42%, #f0a24a 0%, #d97b3a 40%, rgba(230,170,140,0.35) 75%, rgba(255,255,255,0) 100%),
      radial-gradient(ellipse 150px 260px at 72% 55%, rgba(240,200,215,0.7) 0%, rgba(255,255,255,0) 100%),
      linear-gradient(180deg, #ffffff 0%, #fbf3f5 60%, #f7e8ec 100%);
  }
  .title-band {
    position: absolute;
    left: 0; top: 0;
    width: 554px; height: 408px;
    background: linear-gradient(90deg, var(--magenta) 0%, #ad2a7e 60%, var(--magenta-deep) 100%);
    color: var(--paper);
    text-align: center;
  }
  .book-title {
    position: absolute;
    left: 0; right: 0; top: 32px;
    font-family: "Bebas Neue", Impact, sans-serif;
    font-weight: 400;
    font-size: 96px;
    line-height: 76px;
    letter-spacing: 1px;
  }
  .book-subtitle {
    position: absolute;
    left: 0; right: 0; top: 293px;
    font-family: "Bebas Neue", Impact, sans-serif;
    font-weight: 400;
    font-size: 35px;
    line-height: 38px;
    letter-spacing: 2.4px;
  }
  .author-name {
    position: absolute;
    left: 0; right: 0; top: 748px;
    text-align: center;
    font-family: "Oswald", Arial, sans-serif;
    font-weight: 300;
    font-size: 54px;
    line-height: 1;
    letter-spacing: 15px;
    padding-left: 15px;
    white-space: nowrap;
    color: var(--ink-magenta);
  }
</style>
</head>
<body>
<main class="cover-wrap">

  <section class="back-cover">
    <div class="back-artwork" role="img" aria-label="Faded pink photograph of hand-drawn planning sketches: charts, targets, flow diagrams and a glowing light bulb"></div>
    <div class="back-blurb">
      <p>Lorem ipsum dolor sit amet, consectetur adipiscing elit. Duis non cursus lorem. Nunc id ante elit. In malesuada orci aliquam tincidunt bibendum. Quisque neque eros, fermentum ac pretium id, interdum luctus dui. Ut nisi urna, rutrum eu nisi ultrices, tristique dapibus enim. Nunc tempus mi efficitur nulla placerat, id bibendum lacus feugiat. Maecenas faucibus suscipit luctus. Mauris sit amet justo congue elit pellentesque pharetra lacinia eget felis. Vivamus sed mollis sapien.</p>
      <p>Integer euismod ex justo, sollicitudin porttitor odio posuere ac. Aliquam hendrerit accumsan quam, nec interdum ante fringilla in. Aliquam lobortis metus sit amet ornare tempus. Sed tincidunt tellus quis tempor consequat. Aenean eget magna neque. Nam id sollicitudin orci. Donec ut leo ac nibh consectetur vehicula a quis nunc. Donec nec neque quis erat finibus scelerisque. Nullam egestas tempor libero eu consectetur. Ut quis turpis nec mi maximus ultrices at at eros. Maecenas sit amet efficitur tortor.</p>
    </div>
    <div class="isbn-space" aria-hidden="true"></div>
  </section>

  <section class="spine">
    <div class="spine-title">THE COPPER KETTLE HANDBOOK</div>
    <div class="spine-author">MAREN OSEI</div>
  </section>

  <section class="front-cover">
    <div class="front-artwork" role="img" aria-label="Photograph of a glowing vintage light bulb filled with sketched business diagrams, beside a faded second bulb on a white background"></div>
    <header class="title-band">
      <h1 class="book-title">THE COPPER<br>KETTLE<br>HANDBOOK</h1>
      <p class="book-subtitle">A PRACTITIONER´S GUIDE TO BUILDING<br>VIABLE PRODUCTS CUSTOMERS LOVE</p>
    </header>
    <p class="author-name">MAREN OSEI</p>
  </section>

</main>
</body>
</html>
```